Varemo Group Business Card Design

The CEO is looking for a new trendy look for his business card.
You can stay with current branding or come up with something new/creative. It can be 3D, including Medical Office buildings. You can use our logo in a variety of colors. Please include name, title, company name, company website, email address, cell number

Target Market(s)

Real Estate Development and Construction

Industry/Entity Type

Health care real estate

Contact Information for Business Card

Rohesh Kumbar, CEO M-727.418.9062 E-roheshkumbar@varemo.com Address:4100 Lindell Ave, Tampa, FL 33611 www.varemo.com

Font styles to use
Other font styles liked:
• Be creative

Requirements
Must have
• Creative, trendy look
Nice to have
• Please go to our website to get a feel- www. varemo.com
Should not have
• small fonts

```html
<!DOCTYPE html>
<html lang="en">
<head>
<meta charset="utf-8">
<title>Varemo Group Business Card</title>
<link rel="stylesheet" href="https://fonts.googleapis.com/css2?family=Lato:wght@400;700&display=swap">
<style>
  :root {
    --backdrop: #3a3a3a;
    --brand-red: #b01e2b;
    --brand-red-deep: #a51a26;
    --brand-red-light: #c73340;
    --card-white: #ffffff;
    --ink: #1d1d1d;
  }
  * { box-sizing: border-box; margin: 0; padding: 0; }
  html, body { width: 1200px; height: 694px; overflow: hidden; }
  body {
    background: var(--backdrop);
    font-family: "Lato", sans-serif;
    position: relative;
  }
  .card {
    position: absolute;
    top: 187px;
    width: 540px;
    height: 320px;
    border-radius: 26px;
    overflow: hidden;
    box-shadow: 0 14px 30px rgba(0,0,0,0.35);
  }
  .card-front { left: 40px; background: var(--brand-red); }
  .front-texture {
    position: absolute; inset: 0;
    background: linear-gradient(135deg, var(--brand-red-light) 0%, var(--brand-red) 45%, var(--brand-red-deep) 100%);
  }
  .front-wordmark {
    position: absolute; left: 0; right: 0; top: 50%;
    transform: translateY(-50%);
    text-align: center;
    color: var(--card-white);
    font-weight: 700;
    font-size: 40px;
    letter-spacing: -0.5px;
  }
  .card-back { left: 620px; background: var(--card-white); }
  .back-wordmark {
    position: absolute; left: 30px; top: 132px;
    width: 215px;
    color: var(--brand-red);
    font-weight: 700;
    font-size: 40px;
    line-height: 1;
    letter-spacing: -0.5px;
  }
  .divider {
    position: absolute; left: 262px; top: 70px;
    width: 1.5px; height: 180px;
    background: linear-gradient(to bottom, rgba(176,30,43,0), var(--brand-red) 20%, var(--brand-red) 80%, rgba(176,30,43,0));
  }
  .contact {
    position: absolute; left: 282px; top: 76px; right: 20px;
    color: var(--ink);
  }
  .contact-name {
    color: var(--brand-red);
    font-weight: 700;
    font-size: 23px;
    line-height: 1.1;
  }
  .contact-title { font-size: 14px; margin: 2px 0 14px; }
  .contact-list { list-style: none; }
  .contact-item {
    display: flex; align-items: flex-start; gap: 9px;
    font-size: 13.5px; line-height: 1.25; margin-bottom: 6px;
  }
  .contact-icon { width: 14px; height: 14px; flex: none; margin-top: 1px; fill: var(--brand-red); }
</style>
</head>
<body>
  <section class="card card-front">
    <div class="front-texture" role="img" aria-label="Repeated embossed brand name pattern in tonal red"></div>
    <div class="front-wordmark">Varemo</div>
  </section>

  <section class="card card-back">
    <div class="back-wordmark">Varemo Group</div>
    <div class="divider"></div>
    <div class="contact">
      <h1 class="contact-name">Rohesh Kumbar</h1>
      <p class="contact-title">CEO</p>
      <ul class="contact-list">
        <li class="contact-item">
          <svg class="contact-icon" viewBox="0 0 14 14"><path d="M4 1h6a1 1 0 0 1 1 1v10a1 1 0 0 1-1 1H4a1 1 0 0 1-1-1V2a1 1 0 0 1 1-1zm0.6 1.4v8.2h4.8V2.4z"/></svg>
          727.418.9062
        </li>
        <li class="contact-item">
          <svg class="contact-icon" viewBox="0 0 14 14"><path d="M1 3h12v8H1z M1 3l6 4.5L13 3" /><path d="M1.8 4.2L7 8l5.2-3.8" fill="#fff"/></svg>
          roheshkumbar@varemo.com
        </li>
        <li class="contact-item">
          <svg class="contact-icon" viewBox="0 0 14 14"><circle cx="7" cy="7" r="6"/><path d="M4 4.5c1.2 0 1.8.8 1.5 1.8-.3.9.6 1.4.3 2.4M9.5 3.5c-.8.8-.2 1.8.8 2M8.5 11c0-1.2.8-1.6 1.8-1.8" stroke="#fff" stroke-width="1" fill="none"/></svg>
          www.varemo.com
        </li>
        <li class="contact-item">
          <svg class="contact-icon" viewBox="0 0 14 14"><path d="M7 1a4.3 4.3 0 0 1 4.3 4.3C11.3 8.5 7 13 7 13S2.7 8.5 2.7 5.3A4.3 4.3 0 0 1 7 1zm0 2.6a1.7 1.7 0 1 0 0 3.4 1.7 1.7 0 0 0 0-3.4z"/></svg>
          <span>4100 Lindell Ave, Tampa,<br>FL 33611</span>
        </li>
      </ul>
    </div>
  </section>
</body>
</html>
```